Simple Banners for several sites

I'm looking for banners in the following formats for the sites listed bellow:

* Leaderboard
* Wide Skyscraper
* Skyscaper
* Square Button
* Micro bar
* Full banner
* Half Banner
* Medium Rectangle

The websites:
* http://factheap.vornel.com/
* http://pagtrove.com/
* http://netolumba.com/

I would like to get 1 sets of banners for each website, and I'ld like you to submit each set/site independently.

```html
<!DOCTYPE html>
<html lang="en">
<head>
<meta charset="utf-8">
<title>Fact Heap – Banner Set</title>
<link rel="stylesheet" href="https://fonts.googleapis.com/css2?family=Arimo:wght@700&family=Open+Sans:wght@400&display=swap">
<style>
  :root {
    --page-bg: #ebe6df;
    --banner-bg: #ffffff;
    --brand-green: #5c9c3a;
    --button-green: #5b9a3c;
    --ink: #111111;
    --photo-light: #d9dfe6;
    --photo-mid: #5aa9d6;
    --photo-dark: #2b2f36;
  }
  * { margin: 0; padding: 0; box-sizing: border-box; }
  html, body { width: 1200px; height: 900px; overflow: hidden; }
  body { background: var(--page-bg); position: relative; font-family: "Arimo", Arial, sans-serif; }

  .banner { position: absolute; background: var(--banner-bg); overflow: hidden; box-shadow: 0 2px 8px rgba(0,0,0,.12); }
  .banner__photo { position: absolute; left: 0; top: 0; }
  .brand { position: absolute; font-family: "Open Sans", Arial, sans-serif; font-weight: 400; color: var(--brand-green); white-space: nowrap; line-height: 1; }
  .tagline { position: absolute; font-weight: 700; color: var(--ink); line-height: 1.25; }
  .tagline em { font-style: normal; color: var(--brand-green); }
  .cta { position: absolute; background: var(--button-green); color: #fff; font-weight: 700; border-radius: 22px; display: flex; align-items: center; justify-content: center; white-space: nowrap; }
  .url { position: absolute; font-weight: 700; color: var(--ink); font-size: 12px; white-space: nowrap; }

  /* Leaderboard */
  .leaderboard { left: 182px; top: 40px; width: 853px; height: 106px; }
  .leaderboard .tagline { left: 336px; top: 26px; font-size: 20px; text-align: right; }
  .leaderboard .brand { left: 690px; top: 4px; font-size: 31px; }
  .leaderboard .cta { left: 696px; top: 46px; width: 147px; height: 40px; font-size: 21px; }
  .leaderboard .url { right: 4px; bottom: 2px; }

  /* Medium rectangle */
  .rectangle { left: 311px; top: 292px; width: 352px; height: 292px; }
  .rectangle .tagline { left: 3px; top: 153px; font-size: 22px; text-align: right; }
  .rectangle .brand { left: 11px; top: 234px; font-size: 31px; }
  .rectangle .cta { left: 193px; top: 233px; width: 147px; height: 39px; font-size: 21px; }
  .rectangle .url { right: 4px; bottom: 3px; }

  /* Skyscraper */
  .skyscraper { left: 810px; top: 165px; width: 188px; height: 703px; }
  .skyscraper .brand { left: 0; right: 0; top: 28px; text-align: center; font-size: 37px; }
  .skyscraper .tagline { left: 0; right: 0; top: 373px; font-size: 25px; text-align: center; line-height: 1.37; }
  .skyscraper .cta { left: 26px; top: 616px; width: 147px; height: 39px; font-size: 21px; }
  .skyscraper .url { left: 0; right: 0; top: 655px; text-align: center; }
</style>
</head>
<body>

  <section class="banner leaderboard" aria-label="Leaderboard banner">
    <svg class="banner__photo" width="853" height="106" viewBox="0 0 853 106">
      <defs>
        <linearGradient id="lbPhoto" x1="0" y1="0" x2="1" y2="1">
          <stop offset="0" stop-color="var(--photo-light)"/>
          <stop offset=".5" stop-color="var(--photo-mid)"/>
          <stop offset="1" stop-color="var(--photo-dark)"/>
        </linearGradient>
      </defs>
      <polygon points="0,0 330,0 287,106 0,106" fill="url(#lbPhoto)" role="img" aria-label="Hand holding a glowing globe surrounded by connected network icons"/>
      <polygon points="330,0 336,0 293,106 287,106" fill="var(--brand-green)"/>
    </svg>
    <p class="tagline">All the Info from the Internet,<br><em>DUMPED</em> in a simple <em>SITE</em></p>
    <p class="brand">Fact Heap</p>
    <a class="cta">CLICK HERE</a>
    <p class="url">www.factheap.vornel.com</p>
  </section>

  <section class="banner rectangle" aria-label="Medium rectangle banner">
    <svg class="banner__photo" width="352" height="160" viewBox="0 0 352 160">
      <defs>
        <linearGradient id="rectPhoto" x1="0" y1="0" x2="1" y2="1">
          <stop offset="0" stop-color="var(--photo-light)"/>
          <stop offset=".55" stop-color="var(--photo-mid)"/>
          <stop offset="1" stop-color="var(--photo-dark)"/>
        </linearGradient>
      </defs>
      <polygon points="0,0 352,0 352,150 0,121" fill="url(#rectPhoto)" role="img" aria-label="Hand holding a glowing globe surrounded by connected network icons"/>
      <polygon points="0,121 352,150 352,154 0,125" fill="var(--brand-green)"/>
    </svg>
    <p class="tagline">All the Info from the Internet,<br><em>DUMPED</em> in a simple <em>SITE</em></p>
    <p class="brand">Fact Heap</p>
    <a class="cta">CLICK HERE</a>
    <p class="url">www.factheap.vornel.com</p>
  </section>

  <section class="banner skyscraper" aria-label="Skyscraper banner">
    <p class="brand">Fact Heap</p>
    <svg class="banner__photo" width="188" height="370" viewBox="0 0 188 370" style="top:0">
      <defs>
        <linearGradient id="skyPhoto" x1="0" y1="0" x2="1" y2="1">
          <stop offset="0" stop-color="var(--photo-light)"/>
          <stop offset=".45" stop-color="var(--photo-dark)"/>
          <stop offset=".7" stop-color="var(--photo-mid)"/>
          <stop offset="1" stop-color="var(--photo-dark)"/>
        </linearGradient>
      </defs>
      <polygon points="0,90 188,90 188,358 0,303" fill="url(#skyPhoto)" role="img" aria-label="Businessman holding a glowing globe linked to network icons"/>
      <polygon points="0,303 188,358 188,363 0,308" fill="var(--brand-green)"/>
    </svg>
    <p class="tagline">All the Info<br>from the<br>Internet,<br><em>DUMPED</em><br>in a<br>simple <em>SITE</em></p>
    <a class="cta">CLICK HERE</a>
    <p class="url">www.factheap.vornel.com</p>
  </section>

</body>
</html>
```